job vacancy cover page

I need to design a one pager for a job I'd like to apply for. The one I have done looks shit and amateur!! Wanting it to look amazing and professional (Not too professional though as they are pretty young and fun).

```html
<!DOCTYPE html>
<html lang="en">
<head>
<meta charset="utf-8">
<title>Why Me? – Job Application One Pager</title>
<link href="https://fonts.googleapis.com/css2?family=Bebas+Neue&family=Montserrat:wght@400;500;600;700;800&display=swap" rel="stylesheet">
<style>
  :root {
    --blue: #2f7ec1;
    --red: #ec4c68;
    --peach: #faeee3;
    --pink: #fcedf3;
    --mist: #f4f4f5;
    --slate: #3d5560;
    --ink: #1f2a30;
    --body: #4a5a62;
    --gold: #f5bf2e;
    --page: #e9e9ea;
    --white: #ffffff;
  }
  * { box-sizing: border-box; margin: 0; padding: 0; }
  html, body { width: 1200px; height: 800px; overflow: hidden; background: var(--page); }
  body { font-family: "Montserrat", sans-serif; color: var(--ink); }

  .sheet {
    position: absolute; left: 0; top: 65px;
    width: 1200px; height: 670px;
    background: var(--white);
    overflow: hidden;
  }
  .blobs { position: absolute; inset: 0; }

  .display { font-family: "Bebas Neue", sans-serif; font-weight: 400; letter-spacing: 0.5px; }
  .heading { font-family: "Montserrat", sans-serif; font-weight: 800; line-height: 1; }

  .why-me { position: absolute; left: 27px; top: 32px; font-size: 38px; color: var(--white); }

  .art { position: absolute; }
  .art-hero {
    left: 212px; top: 18px; width: 298px; height: 300px;
    background: linear-gradient(170deg, #f3d23a 0%, #ec4c68 50%, #2c2a2e 100%);
    opacity: .85;
    clip-path: polygon(0 0, 165px 0, 165px 30px, 298px 25px, 298px 75px, 165px 112px, 165px 100%, 0 100%);
  }
  .art-trophy { left: 542px; top: 28px; width: 82px; height: 160px; border-radius: 14px;
    background: linear-gradient(180deg, #f7cf4a 0%, #e2a81e 70%, #7a4a32 100%); opacity: .85; }
  .art-ladder { left: 828px; top: 45px; width: 110px; height: 290px; border-radius: 14px;
    background: linear-gradient(180deg, #f08a6f 0%, #3f4b52 100%); opacity: .8; }

  .superhero-title { position: absolute; left: 40px; top: 163px; }
  .superhero-title .small { color: var(--blue); font-size: 18px; display: block; }
  .superhero-title .big { color: var(--red); font-size: 22px; display: block; margin-top: 1px; }
  .lead { position: absolute; left: 40px; top: 215px; font-size: 11.5px; font-weight: 700; line-height: 1.2; width: 150px; }

  .powers { position: absolute; left: 57px; top: 253px; list-style: none; }
  .powers li { display: flex; align-items: center; height: 30px; }
  .powers .num { width: 21px; height: 21px; border-radius: 50%; background: var(--red); color: var(--white);
    font-size: 13px; font-weight: 700; display: flex; align-items: center; justify-content: center; position: relative; z-index: 1; }
  .powers .pill { background: var(--blue); color: var(--white); font-size: 11.5px; font-weight: 500;
    padding: 2px 9px 2px 13px; margin-left: -6px; border-radius: 0 6px 6px 0; }

  .success-title { position: absolute; left: 636px; top: 110px; }
  .success-title .small { color: var(--blue); font-size: 18px; display: block; }
  .success-title .big { color: var(--red); font-size: 22px; display: block; }

  .passion-title { position: absolute; left: 953px; top: 117px; color: var(--red); font-size: 22px; }

  .star-list { position: absolute; list-style: none; font-size: 11.5px; line-height: 1.3; color: var(--ink); }
  .star-list li { display: flex; gap: 9px; align-items: flex-start; }
  .star-list svg { flex: none; width: 17px; height: 17px; margin-top: -3px; }
  .success-list { left: 443px; top: 213px; width: 360px; }
  .success-list li { margin-bottom: 13px; }
  .success-list svg { fill: var(--gold); }
  .passion-list { left: 966px; top: 182px; width: 222px; }
  .passion-list li { margin-bottom: 14px; }
  .passion-list li:not(:last-child) span { max-width: 180px; }
  .passion-list svg { fill: var(--red); }

  .section-rule { position: absolute; top: 457px; height: 1px; background: #e6a89a; }
  .rule-left { left: 20px; width: 240px; }
  .rule-right { left: 534px; width: 650px; }
  .company-title { position: absolute; left: 258px; top: 431px; width: 276px; text-align: center; font-size: 43px; color: var(--blue); }

  .column { position: absolute; top: 507px; }
  .column h2 { font-family: "Montserrat", sans-serif; font-weight: 800; font-size: 18.8px; letter-spacing: .5px; margin-bottom: 13px; }
  .column ul { list-style: none; font-size: 12px; color: var(--body); }
  .column li { display: flex; align-items: center; gap: 9px; height: 23px; }
  .column svg { width: 13px; height: 13px; flex: none; }
  .col-offer { left: 68px; }
  .col-offer h2 { color: #52707d; }
  .col-offer svg { fill: #52707d; }
  .col-offer ul { margin-left: 8px; }
  .col-projects { left: 353px; }
  .col-projects h2 { color: var(--slate); }
  .col-projects svg { fill: var(--slate); }
  .col-projects ul { margin-left: 8px; }
  .col-values { left: 846px; }
  .col-values h2 { color: var(--ink); }
  .col-values svg { fill: var(--ink); }
  .col-values ul { margin-left: 24px; }
</style>
</head>
<body>
<svg width="0" height="0" style="position:absolute">
  <defs>
    <symbol id="star" viewBox="0 0 24 24"><path d="M12 1.5l3.1 7 7.6.7-5.8 5 1.8 7.5L12 17.8l-6.7 3.9 1.8-7.5-5.8-5 7.6-.7z"/></symbol>
  </defs>
</svg>

<main class="sheet">
  <svg class="blobs" viewBox="0 0 1200 670" preserveAspectRatio="none" aria-hidden="true">
    <path fill="var(--pink)" d="M830,0 H1200 V392 C1130,372 1050,405 965,415 C880,425 790,428 730,405 C820,370 890,335 855,262 C815,190 805,80 830,0Z"/>
    <path fill="var(--peach)" d="M500,0 H830 C815,40 830,70 870,85 C800,110 790,170 820,230 C850,290 800,355 700,362 C610,368 560,405 470,400 C400,396 385,330 390,270 C395,200 430,140 470,90 C500,55 490,20 500,0Z"/>
    <path fill="var(--mist)" d="M0,120 C60,126 140,120 170,100 L210,90 C260,120 330,150 380,180 C420,210 400,290 390,330 C370,395 300,418 220,415 C130,410 50,385 0,355Z"/>
    <path fill="var(--blue)" d="M0,0 H213 C195,45 175,80 158,100 C135,128 60,132 0,126Z"/>
  </svg>

  <h1 class="why-me display">Why me?</h1>

  <div class="art art-hero" role="img" aria-label="Illustration of a woman in a superhero costume with a flowing red cape"></div>
  <div class="art art-trophy" role="img" aria-label="Illustration of a gold trophy cup"></div>
  <div class="art art-ladder" role="img" aria-label="Illustration of a woman climbing a ladder while another person steadies it"></div>

  <h2 class="superhero-title heading"><span class="small">IF I WAS A</span><span class="big">SUPERHERO</span></h2>
  <p class="lead">My four superpowers would be:</p>
  <ol class="powers">
    <li><span class="num">1</span><span class="pill">Proactiveness</span></li>
    <li><span class="num">2</span><span class="pill">Creativity</span></li>
    <li><span class="num">3</span><span class="pill">Pride in my work</span></li>
    <li><span class="num">4</span><span class="pill">Organisational skills</span></li>
  </ol>

  <h2 class="success-title heading"><span class="small">SOME OF MY</span><span class="big">SUCCESS</span></h2>
  <ul class="star-list success-list">
    <li><svg><use href="#star"/></svg><span>Increased client workshops by 85% across accounts.</span></li>
    <li><svg><use href="#star"/></svg><span>Delivered double digit revenue increase.</span></li>
    <li><svg><use href="#star"/></svg><span>Re-designed workshops for virtual delivery,<br>maintaining key relationships.</span></li>
  </ul>

  <h2 class="passion-title heading">PASSION</h2>
  <ul class="star-list passion-list">
    <li><svg><use href="#star"/></svg><span>The development of others and / or their teams.</span></li>
    <li><svg><use href="#star"/></svg><span>Helping people learn and be successful in life and in their careers.</span></li>
    <li><svg><use href="#star"/></svg><span>Exceptional client experiences</span></li>
  </ul>

  <div class="section-rule rule-left"></div>
  <h2 class="company-title display">Why Bright Arc?</h2>
  <div class="section-rule rule-right"></div>

  <section class="column col-offer">
    <h2>WHAT YOU OFFER</h2>
    <ul>
      <li><svg><use href="#star"/></svg>Learning &amp; Developing</li>
      <li><svg><use href="#star"/></svg>Team</li>
      <li><svg><use href="#star"/></svg>Flexibility</li>
      <li><svg><use href="#star"/></svg>Fun</li>
    </ul>
  </section>

  <section class="column col-projects">
    <h2>INTERESTING PROJECTS</h2>
    <ul>
      <li><svg><use href="#star"/></svg>Norvale - Leadership development and team effectiveness</li>
      <li><svg><use href="#star"/></svg>Kestrel &amp; Co – Change management for true transformation</li>
      <li><svg><use href="#star"/></svg>Halcyon – Customer centricity at Australia's most iconic department store</li>
    </ul>
  </section>

  <section class="column col-values">
    <h2>VALUES THAT STOOD OUT</h2>
    <ul>
      <li><svg><use href="#star"/></svg>Change for the better</li>
      <li><svg><use href="#star"/></svg>Excellence – not mediocre</li>
      <li><svg><use href="#star"/></svg>Put your heart into it and give a shit</li>
      <li><svg><use href="#star"/></svg>Going the extra mile</li>
      <li><svg><use href="#star"/></svg>Take risks</li>
    </ul>
  </section>
</main>
</body>
</html>
```